Coral Pillow Depot Website

Need a design for a local Miami mattress store.
The store is called Coral Pillow Depot.
need it to be something that customers can find on the internet and will
give them my location, they need to know i have the same brand mattress as the other store except i have them at almost half the price.

the office phone number is (786)555-0147
the office address is: 4721 sw Heron Glade Ave, Miami FL 33190

included is the logo, id like to stick the with white and teal design

here are is an excerpt that can or cannot be included

"We are a premium mattress discount outlet store located in South Florida; offering Free Delivery to Broward Miami-Dade, the Keys, and Palm Beach.

We carry the best brands in the market: Harlow DreamNest; Brovik SpineEase, Kendal & Pryce, Tarvin, among others.

We are open 7 days a week, and we are accessible from all major highways. We are a family business and our goal is to provide you with the most comfortable and best quality mattress at a price that has no competition. Come visit us and take a look at our large inventory selection."

```html
<!DOCTYPE html>
<html lang="en">
<head>
<meta charset="utf-8">
<title>Coral Pillow Depot</title>
<link href="https://fonts.googleapis.com/css2?family=Montserrat:wght@300;400;500;600;700&display=swap" rel="stylesheet">
<style>
  :root {
    --teal: #4fa3c7;
    --teal-panel: #55a8cb;
    --navy: #0e4a66;
    --ink: #2b2b2b;
    --muted: #555;
    --dark-bar: #2e2e2e;
    --caption: #1c1c1c;
    --button-dark: #263238;
    --white: #fff;
    --rule: #e6e6e6;
  }
  * { box-sizing: border-box; margin: 0; padding: 0; }
  html, body { width: 755px; height: 1200px; overflow: hidden; background: var(--white); }
  body { font-family: "Montserrat", sans-serif; color: var(--ink); position: relative; }
  .abs { position: absolute; }

  /* top bar */
  .topbar { left: 0; top: 0; width: 755px; height: 28px; background: var(--teal); color: var(--white); font-size: 8px; }
  .follow { left: 78px; top: 9px; font-weight: 600; font-size: 7.5px; }
  .social { left: 128px; top: 6px; display: flex; gap: 5px; }
  .social span { width: 16px; height: 16px; border-radius: 50%; background: #8cc6de; display: block; }
  .account { right: 78px; top: 8px; display: flex; align-items: center; gap: 4px; font-size: 8.5px; white-space: nowrap; }
  .account .login { color: var(--navy); font-weight: 700; }

  /* navigation */
  .brand { left: 87px; top: 48px; font-size: 15px; font-weight: 500; color: var(--navy); }
  .nav { right: 77px; top: 55px; display: flex; gap: 22px; font-size: 8.5px; text-transform: uppercase; color: #333; }
  .nav-rule { left: 0; top: 90px; width: 755px; height: 1px; background: var(--rule); }
  .tagline { left: 0; top: 105px; width: 755px; text-align: center; font-size: 16px; font-weight: 300; color: var(--muted); }

  /* hero */
  .feature-photo { left: 79px; top: 142px; width: 211px; height: 123px; background: linear-gradient(160deg, #f3f1ea 0%, #e6e1d3 55%, #cfc8b6 100%); }
  .feature-title { left: 88px; top: 158px; font-size: 11px; font-weight: 400; }
  .feature-arrows { left: 264px; top: 158px; }
  .price { left: 221px; top: 223px; width: 54px; height: 54px; border-radius: 50%; background: var(--teal); color: var(--white); font-size: 16px; font-weight: 300; display: flex; align-items: center; justify-content: center; }
  .product-bar { left: 79px; top: 265px; width: 211px; height: 55px; background: var(--dark-bar); color: var(--white); }
  .product-kicker { left: 11px; top: 15px; font-size: 8px; }
  .product-name { left: 11px; top: 28px; font-size: 10.5px; font-weight: 600; }
  .buy-now { left: 135px; top: 19px; width: 71px; height: 21px; background: var(--teal); font-size: 9px; font-weight: 700; display: flex; align-items: center; justify-content: center; }
  .promo { left: 79px; top: 320px; width: 211px; height: 178px; background: var(--teal-panel); color: var(--white); text-align: center; }
  .promo-kicker { left: 0; top: 13px; width: 100%; font-size: 12px; font-weight: 400; }
  .promo-name { left: 0; top: 24px; width: 100%; font-size: 52px; font-weight: 700; color: var(--navy); letter-spacing: -1px; line-height: 1; }
  .promo-sub { left: 0; top: 73px; width: 100%; font-size: 40px; font-weight: 300; line-height: 1; }
  .collections { left: 22px; top: 132px; width: 154px; height: 27px; background: var(--button-dark); font-size: 10px; white-space: nowrap; display: flex; align-items: center; justify-content: center; }
  .slide-photo { left: 290px; top: 142px; width: 387px; height: 310px; background: linear-gradient(180deg, #8a7a66 0%, #a99880 40%, #f2f0ec 62%, #e8e6e2 100%); }
  .slide-caption { left: 290px; top: 452px; width: 387px; height: 46px; background: var(--caption); color: var(--white); font-size: 11px; font-weight: 300; }
  .slide-caption p { position: absolute; left: 15px; top: 17px; white-space: nowrap; }
  .dots { right: 12px; top: 19px; display: flex; gap: 5px; }
  .dots span { width: 7px; height: 7px; background: var(--white); display: block; }
  .dots span:first-child { background: var(--teal); }

  /* types */
  .types { left: 79px; top: 521px; color: var(--teal); line-height: 0.95; font-weight: 400; }
  .types .big { font-size: 52px; }
  .types .mid { font-size: 34px; }
  .types .low { font-size: 42px; }
  .type-card { top: 517px; width: 190px; height: 150px; text-align: center; }
  .type-circle { position: absolute; top: 0; width: 112px; height: 112px; border-radius: 50%; background: var(--teal); }
  .type-photo { position: absolute; top: 26px; width: 110px; height: 72px; border-radius: 6px; background: linear-gradient(180deg, #ffffff 0%, #e4e7ea 100%); box-shadow: 0 6px 10px rgba(0,0,0,0.18); }
  .type-label { position: absolute; left: 0; top: 125px; width: 100%; font-size: 14px; color: #333; white-space: nowrap; }

  /* welcome */
  .welcome { left: 79px; top: 684px; width: 598px; height: 347px; background: linear-gradient(180deg, #1b86c9 0%, #4fb0e3 38%, #bfe2f3 62%, #4fb7c4 74%, #d9c6a3 90%, #cdb894 100%); }
  .welcome-tower { left: 79px; top: 716px; width: 320px; height: 300px; background: linear-gradient(160deg, #f2a02a 0%, #e8661d 50%, #d2256a 100%); border-radius: 4px; opacity: 0.9; }
  .welcome-title { left: 395px; top: 716px; color: var(--white); font-weight: 400; line-height: 1; }
  .welcome-title .one { font-size: 38px; display: block; }
  .welcome-title .two { font-size: 30px; display: block; margin-top: -2px; }
  .welcome-copy { left: 396px; top: 801px; width: 240px; color: var(--white); font-size: 8.3px; line-height: 16.4px; }

  /* partners */
  .partners { left: 79px; top: 1031px; width: 598px; height: 72px; background: var(--white); box-shadow: 0 8px 14px rgba(0,0,0,0.08); display: flex; justify-content: space-around; align-items: center; padding: 0 14px; font-size: 11px; font-weight: 600; color: #1d3f6b; }

  /* footer */
  .footer { left: 0; top: 1128px; width: 755px; height: 72px; background: var(--teal); color: #18384a; font-size: 8.5px; }
  .footer-links { left: 78px; top: 19px; display: flex; gap: 11px; }
  .footer-legal { left: 78px; top: 41px; font-size: 8px; white-space: nowrap; }
  .subscribe { left: 439px; top: 16px; display: flex; height: 29px; }
  .email { width: 165px; background: var(--white); color: #aaa; display: flex; align-items: center; gap: 5px; padding-left: 8px; font-size: 8.5px; }
  .subscribe-btn { width: 73px; border: 1px solid var(--white); color: var(--white); font-weight: 700; display: flex; align-items: center; justify-content: center; }
</style>
</head>
<body>

<header class="abs topbar">
  <span class="abs follow">Follow Us on</span>
  <div class="abs social"><span></span><span></span><span></span></div>
  <div class="abs account">
    <svg width="13" height="11" viewBox="0 0 13 11" fill="none" stroke="#fff" stroke-width="1.1"><path d="M0.5 1h2l1.5 6h7l1.3-4.5H3.3"/><circle cx="5" cy="9.5" r="0.9"/><circle cx="10" cy="9.5" r="0.9"/></svg>
    <span>My Cart ($0.00) &nbsp;| Support | Help &nbsp;| &nbsp;</span><span class="login">LOGIN</span>
  </div>
</header>

<div class="abs brand">Coral Pillow Depot</div>
<nav class="abs nav">
  <span>Home</span><span>About Us</span><span>Products</span><span>Store Locations</span><span>Contact Us</span>
</nav>
<div class="abs nav-rule"></div>

<h1 class="abs tagline">We sell both branded mattress and cheap ones too</h1>

<section>
  <div class="abs feature-photo" role="img" aria-label="Folded white bedding and pillows with lavender"></div>
  <h2 class="abs feature-title">Featured Products</h2>
  <svg class="abs feature-arrows" width="20" height="12" viewBox="0 0 20 12" fill="none" stroke="#555" stroke-width="1.3"><path d="M6 1l-5 5 5 5"/><path d="M14 1l5 5-5 5"/></svg>
  <div class="abs price">$230</div>
  <div class="abs product-bar">
    <span class="abs product-kicker">Quality Mattress</span>
    <span class="abs product-name">Coral Pillow</span>
    <span class="abs buy-now">BUY NOW</span>
  </div>
  <div class="abs promo">
    <p class="abs promo-kicker">HAVE A GOOD SLEEP WITH</p>
    <p class="abs promo-name">coral</p>
    <p class="abs promo-sub">pillow</p>
    <span class="abs collections">VIEW OUR COLLECTIONS</span>
  </div>
  <div class="abs slide-photo" role="img" aria-label="Bedroom with a white bed, cushions, lamp and striped blind"></div>
  <div class="abs slide-caption">
    <p>Same brands as the big stores at almost half the price</p>
    <div class="abs dots"><span></span><span></span><span></span><span></span></div>
  </div>
</section>

<section>
  <h2 class="abs types">
    <span class="big">Types</span><br>
    <span class="mid">of matress</span><br>
    <span class="low">available</span>
  </h2>
  <div class="abs type-card" style="left:271px">
    <span class="type-circle" style="left:37px"></span>
    <span class="type-photo" style="left:15px" role="img" aria-label="Thick white pillow-top mattress"></span>
    <span class="type-label">High -Quality Mattress</span>
  </div>
  <div class="abs type-card" style="left:486px">
    <span class="type-circle" style="left:42px"></span>
    <span class="type-photo" style="left:40px" role="img" aria-label="Quilted mattress with two dark pillows"></span>
    <span class="type-label">Low -Quality Mattress</span>
  </div>
</section>

<section>
  <div class="abs welcome" role="img" aria-label="Miami beach scene under a blue sky"></div>
  <div class="abs welcome-tower" role="img" aria-label="Colourful striped lifeguard tower with a green flag"></div>
  <h2 class="abs welcome-title"><span class="one">Welcome to</span><span class="two">coral pillow</span></h2>
  <p class="abs welcome-copy">Lorem Ipsum is simply dummy text of the printing and typesetting industry. Lorem Ipsum has been the industry's standard dummy text ever since the 1500s, when an unknown printer took a galley of type and scrambled it to make a type specimen book. It has survived not only five centuries, but also the leap into electronic typesetting, remaining essentially unchanged. It was popularised in the 1960s with the release of Printwell sheets containing Lorem Ipsum passages, and more recently with desktop publishing software like Folio Layout including versions of Lorem Ipsum.</p>
</section>

<div class="abs partners">
  <span>Restline</span><span>Velora</span><span>Loftaire</span><span>Novasleep</span><span>Brennick</span><span>Ashgrove</span><span>Restline Plus</span><span>Dozewell</span>
</div>

<footer class="abs footer">
  <div class="abs footer-links">
    <span>Home</span><span>|</span><span>About us</span><span>|</span><span>Products</span><span>|</span><span>Store Locations</span><span>|</span><span>Contact Us</span>
  </div>
  <p class="abs footer-legal">4721 sw Heron Glade Ave, Miami FL 33190 &nbsp;| (786)555-0147 &nbsp;| privacy policy &nbsp;| Terms &amp; Conditions</p>
  <div class="abs subscribe">
    <div class="email">
      <svg width="16" height="11" viewBox="0 0 16 11" fill="none" stroke="#4fa3c7" stroke-width="1.2"><rect x="0.6" y="0.6" width="14.8" height="9.8"/><path d="M0.6 0.6L8 6l7.4-5.4"/></svg>
      <span>E-Mail Address</span>
    </div>
    <div class="subscribe-btn">SUBSCRIBE</div>
  </div>
</footer>

</body>
</html>
```